First Aid Training business needs business card design

We would like a double sided business card designed for a first aid training business - Brindlewood First Aid. We provide first aid training and , WHS (work, health and safety) training.

The attached word document contains the key information we would like on each side of the business card.

Final design needs to be delivered in print ready format, along with the original file.

```html
<!DOCTYPE html>
<html lang="en">
<head>
<meta charset="utf-8">
<title>Brindlewood First Aid – Business Card</title>
<link rel="stylesheet" href="https://fonts.googleapis.com/css2?family=Montserrat:wght@600;700;800&family=Roboto:wght@400&display=swap">
<style>
  :root {
    --bg: #d6d6d6;
    --card: #eeeeef;
    --ink: #111111;
    --red: #d71f26;
    --grey: #7a7a7a;
  }
  * { margin: 0; padding: 0; box-sizing: border-box; }
  html, body { width: 1200px; height: 1101px; overflow: hidden; }
  body { background: var(--bg); position: relative; font-family: "Roboto", Arial, sans-serif; color: var(--ink); }

  .card {
    position: absolute; width: 302px; height: 534px;
    background: var(--card);
    box-shadow: 0 14px 24px rgba(0,0,0,0.18);
  }
  .card--front { left: 246px; top: 266px; }
  .card--back { left: 642px; top: 265px; }

  .centered { position: absolute; left: 0; width: 100%; text-align: center; }

  .person { top: 62px; font-family: "Montserrat", Arial, sans-serif; font-weight: 800; font-size: 39px; line-height: 44px; letter-spacing: 0.5px; }
  .person__first { color: var(--red); }
  .person__last { color: var(--ink); }

  .brand-mark { position: absolute; border-radius: 50%; background: var(--red); }
  .card--front .brand-mark { left: 111px; top: 220px; width: 80px; height: 80px; }
  .card--front .brand-name { top: 320px; font-family: "Montserrat", Arial, sans-serif; font-weight: 700; font-size: 14px; color: var(--ink); letter-spacing: 0.5px; }

  .contact-icons { position: absolute; top: 376px; left: 58px; width: 186px; height: 26px; }
  .contact { top: 414px; font-size: 16.5px; line-height: 21px; }

  .headline { top: 46px; font-family: "Montserrat", Arial, sans-serif; font-weight: 700; font-size: 19px; line-height: 22px; }
  .benefits { top: 98px; list-style: none; font-size: 16.5px; line-height: 20px; }
  .benefits li { margin-bottom: 5px; }
  .benefits li::before { content: ""; display: inline-block; width: 6px; height: 6px; border-radius: 50%; background: var(--red); margin-right: 9px; vertical-align: 3px; }
  .benefits .indent { display: block; }
  .divider { position: absolute; top: 206px; left: 99px; width: 104px; height: 2px; background: var(--red); border-radius: 1px; }
  .services { top: 226px; font-family: "Montserrat", Arial, sans-serif; font-weight: 700; font-size: 16px; line-height: 20px; }

  .card--back .brand-mark { left: 111px; top: 330px; width: 80px; height: 80px; }
  .card--back .brand-name { top: 432px; font-family: "Montserrat", Arial, sans-serif; font-weight: 600; font-size: 22px; line-height: 26px; color: var(--ink); }
</style>
</head>
<body>

<section class="card card--front">
  <h1 class="centered person">
    <span class="person__first">DANIEL</span><br>
    <span class="person__last">HART</span>
  </h1>

  <span class="brand-mark"></span>
  <p class="centered brand-name">BRINDLEWOOD FIRST AID</p>

  <svg class="contact-icons" viewBox="0 0 186 26" aria-hidden="true">
    <line x1="0" y1="13" x2="40" y2="13" stroke="#111" stroke-width="2"/>
    <line x1="146" y1="13" x2="186" y2="13" stroke="#111" stroke-width="2"/>
    <circle cx="59" cy="13" r="12" fill="#d71f26"/>
    <rect x="54.5" y="5.5" width="9" height="15" rx="1.5" fill="none" stroke="#fff" stroke-width="1.6"/>
    <circle cx="93" cy="13" r="12" fill="#d71f26"/>
    <rect x="86" y="8.5" width="14" height="9.5" rx="1" fill="none" stroke="#fff" stroke-width="1.5"/>
    <polyline points="86,9 93,14 100,9" fill="none" stroke="#fff" stroke-width="1.5"/>
    <circle cx="127" cy="13" r="12" fill="#d71f26"/>
    <circle cx="127" cy="13" r="7" fill="none" stroke="#fff" stroke-width="1.4"/>
    <ellipse cx="127" cy="13" rx="3" ry="7" fill="none" stroke="#fff" stroke-width="1.2"/>
    <line x1="120" y1="13" x2="134" y2="13" stroke="#fff" stroke-width="1.2"/>
  </svg>

  <p class="centered contact">
    0412 555 019<br>
    help@brindlewoodfirstaid.com.au<br>
    www.brindlewoodfirstaid.com.au
  </p>
</section>

<section class="card card--back">
  <h2 class="centered headline">Onsite Training<br>- We can come to you</h2>

  <ul class="centered benefits">
    <li>Time efficient</li>
    <li>Minimise downtime<span class="indent">for your team</span></li>
    <li>Cost effective</li>
  </ul>

  <span class="divider"></span>

  <p class="centered services">First Aid Training<br>WHS Training</p>

  <span class="brand-mark"></span>
  <p class="centered brand-name">BRINDLEWOOD<br>FIRST AID TRAINING</p>
</section>

</body>
</html>
```